Webbanner-Design für Tanzschule
Zielgruppe
Wir sind eine Tanzschule und benötigen einen werbebanner.
Aufgabenstellung
Hierfür benötigen wir eine Banner (Haeder): https://www.tanzkreisnord.de/page/3/
Es soll enthalten sein:
Logo: Ritmo del Alba
Angebot: Salsa, Bachata, Kizomba, Zouk, Lady- & Menstyle
Einstiegsmöglichkeiten Jederzeit
Gratis Schnupperstunde - es soll zum Klick animieren
Es soll dich zum Tanzen einladen und professionell wirken.
Die Bilder sind nur eine Idee.
https://www.ritmo-del-alba.de/
It should contain:
Offer: Salsa, Bachata, Kizomba, Zouk, Lady- & Menstyle
Join the courses every month
Free trial lesson - it should encourage you to click
It should invite you to dance and look professional!
The pictures are just an idea!

```html
<!DOCTYPE html>
<html lang="de">
<head>
<meta charset="utf-8">
<title>Ritmo del Alba – Tanzschule Banner</title>
<link rel="stylesheet" href="https://fonts.googleapis.com/css2?family=Figtree:ital,wght@0,400;0,600;1,700&display=swap">
<style>
  :root {
    --page-bg: #ececec;
    --yellow: #ffdc00;
    --magenta: #ad1b5e;
    --white: #ffffff;
    --grey-text: #cfcfcf;
  }
  html, body {
    margin: 0;
    padding: 0;
    width: 1200px;
    height: 529px;
    overflow: hidden;
    background: var(--page-bg);
    font-family: "Figtree", Arial, sans-serif;
  }
  .banner-frame {
    position: absolute;
    left: 0;
    top: 54px;
    width: 1280px;
    height: 449px;
    transform: scale(0.9375);
    transform-origin: top left;
    overflow: hidden;
  }
  .banner-art {
    position: absolute;
    inset: 0;
  }
  .brand {
    position: absolute;
    left: 38px;
    top: 40px;
    color: var(--white);
  }
  .brand-name {
    display: flex;
    align-items: center;
    gap: 14px;
    font-size: 42px;
    font-weight: 600;
    line-height: 1;
  }
  .brand-dot {
    width: 32px;
    height: 32px;
    border-radius: 50%;
    background: var(--magenta);
  }
  .brand-tagline {
    margin: 12px 0 0 72px;
    font-size: 16px;
    font-weight: 400;
    color: var(--grey-text);
  }
  .offer-list {
    position: absolute;
    left: 48px;
    top: 166px;
    margin: 0;
    padding: 0;
    list-style: none;
  }
  .offer-item {
    display: flex;
    align-items: center;
    height: 49.5px;
    font-size: 30px;
    font-style: italic;
    font-weight: 700;
    color: var(--white);
  }
  .offer-item::before {
    content: "";
    width: 31px;
    height: 31px;
    border-radius: 50%;
    background: var(--yellow);
    margin-right: 26px;
    flex: none;
  }
  .entry-note {
    position: absolute;
    left: 840px;
    width: 400px;
    top: 268px;
    text-align: center;
    font-size: 29px;
    font-style: italic;
    font-weight: 700;
    line-height: 37px;
    color: var(--yellow);
    text-shadow: 0 1px 6px rgba(0,0,0,0.45);
  }
  .trial-button {
    position: absolute;
    left: 854px;
    top: 363px;
    width: 390px;
    height: 62px;
    background: var(--magenta);
    display: flex;
    align-items: center;
    justify-content: center;
    font-size: 30px;
    font-style: italic;
    font-weight: 700;
    color: var(--white);
    text-decoration: none;
  }
  .trial-button .highlight { color: var(--yellow); margin-right: 7px; }
</style>
</head>
<body>
  <div class="banner-frame">
    <svg class="banner-art" width="1280" height="449" viewBox="0 0 1280 449" xmlns="http://www.w3.org/2000/svg">
      <defs>
        <radialGradient id="wall" cx="0.5" cy="0.35" r="0.8">
          <stop offset="0" stop-color="#5c5c5c"/>
          <stop offset="0.6" stop-color="#363636"/>
          <stop offset="1" stop-color="#1b1b1b"/>
        </radialGradient>
        <linearGradient id="floor" x1="0" x2="0" y1="0" y2="1">
          <stop offset="0" stop-color="#2a2a2a" stop-opacity="0"/>
          <stop offset="0.35" stop-color="#6a6a6a" stop-opacity="0.55"/>
          <stop offset="1" stop-color="#8a8a8a" stop-opacity="0.6"/>
        </linearGradient>
        <radialGradient id="coupleTone" cx="0.5" cy="0.5" r="0.5">
          <stop offset="0" stop-color="#d8d8d6" stop-opacity="0.85"/>
          <stop offset="0.3" stop-color="#7f93ad" stop-opacity="0.8"/>
          <stop offset="0.7" stop-color="#3d5273" stop-opacity="0.6"/>
          <stop offset="1" stop-color="#2a3a52" stop-opacity="0"/>
        </radialGradient>
        <radialGradient id="closeupTone" cx="0.5" cy="0.45" r="0.55">
          <stop offset="0" stop-color="#5f7698" stop-opacity="0.95"/>
          <stop offset="0.55" stop-color="#3a4e6c" stop-opacity="0.85"/>
          <stop offset="1" stop-color="#23324a" stop-opacity="0"/>
        </radialGradient>
        <linearGradient id="shirtTone" x1="0" x2="0" y1="0" y2="1">
          <stop offset="0" stop-color="#f2f2f0" stop-opacity="0.9"/>
          <stop offset="1" stop-color="#c9c9c6" stop-opacity="0"/>
        </linearGradient>
      </defs>
      <rect width="1280" height="449" fill="url(#wall)" role="img" aria-label="Tanzstudio mit grauer Betonwand"/>
      <rect x="0" y="330" width="1280" height="119" fill="url(#floor)" role="img" aria-label="Grauer Holzdielenboden"/>
      <g role="img" aria-label="Foto eines Tanzpaares in Jeans und weißen Oberteilen beim Salsa">
        <ellipse cx="560" cy="215" rx="190" ry="230" fill="url(#coupleTone)"/>
      </g>
      <g role="img" aria-label="Nahaufnahme eines tanzenden Paares in Jeans mit weißen Oberteilen">
        <ellipse cx="1060" cy="250" rx="300" ry="280" fill="url(#closeupTone)"/>
        <ellipse cx="1120" cy="20" rx="150" ry="80" fill="url(#shirtTone)"/>
      </g>
      <circle cx="781" cy="0" r="98" fill="var(--yellow)"/>
      <circle cx="916" cy="50" r="25" fill="var(--yellow)"/>
      <circle cx="1300" cy="209" r="97" fill="var(--magenta)"/>
      <circle cx="0" cy="460" r="66" fill="var(--yellow)"/>
      <circle cx="476" cy="494" r="75" fill="var(--magenta)"/>
    </svg>

    <div class="brand">
      <div class="brand-name">Ritmo del Alba <span class="brand-dot"></span></div>
      <div class="brand-tagline">Salsa · Bachata · Kizomba</div>
    </div>

    <ul class="offer-list">
      <li class="offer-item">Salsa</li>
      <li class="offer-item">Bachata</li>
      <li class="offer-item">Kizomba</li>
      <li class="offer-item">Zouk Lady- &amp; Menstyle</li>
    </ul>

    <div class="entry-note">Einstiegsmöglichkeiten<br>Jederzeit</div>

    <a class="trial-button" href="https://www.ritmo-del-alba.de/"><span class="highlight">GRATIS</span>Schnupperstunde</a>
  </div>
</body>
</html>
```